Home Inspection Report Cover Page- House report

We complete home inspections. This is the very first cover page of our report. We are looking to redesign the front cover page for our inspection reports. The image of the home will change as the property changes. I am providing some initial thoughts for designs. But we are willing to see new and creative designs. We are the predominant company in our industry.

Here is another link to see the first page that we currently have
https://harborviewchecks.com/wp-content/uploads/2019/11/NoPoolNewHomeSample.pdf

People print these reports out so the ink level may be a consideration.

We are looking for a modern design that presents us as an authority.

8.5 x 11

Target Market(s)

Home Buyers and Real Estate Agent

Industry/Entity Type

Home Inspection

Requirements
Must have
• Brand Consistency- Our colors can be found at harborviewchecks.com or in the uploaded Trifold named HC_Trifold

Place for a photograph of the front of a home to be
Nice to have
• Color Gradients

```html
<!DOCTYPE html>
<html lang="en">
<head>
<meta charset="utf-8">
<title>Harborview Checks – Inspection Report Cover</title>
<link href="https://fonts.googleapis.com/css2?family=Montserrat:ital,wght@0,500;0,600;0,700;0,800;1,500&family=Open+Sans:ital,wght@0,400;0,600;1,400&display=swap" rel="stylesheet">
<style>
  :root {
    --brand-blue: #2f5fa6;
    --brand-blue-dark: #264f8f;
    --brand-green: #8cc63f;
    --brand-gray: #a7a9ac;
    --paper: #ffffff;
    --backdrop: #2b2b2d;
    --photo-sky: #dfe9f2;
    --photo-wall: #eef0ef;
    --photo-pool: #5fa9c2;
    --photo-lawn: #8fbf5a;
  }
  * { box-sizing: border-box; margin: 0; padding: 0; }
  html, body { width: 1200px; height: 789px; overflow: hidden; }
  body { background: var(--backdrop); position: relative; font-family: "Open Sans", sans-serif; }

  .cover {
    position: absolute; left: 314px; top: 24px;
    width: 572px; height: 740px;
    background: var(--paper); overflow: hidden;
    box-shadow: 0 10px 30px rgba(0,0,0,.45);
  }
  .cover__shapes { position: absolute; inset: 0; }

  .brand { position: absolute; left: 34px; top: 42px; display: flex; align-items: center; gap: 18px; }
  .brand__mark { width: 78px; height: 78px; border-radius: 50%; border: 5px solid var(--brand-blue); flex: none; }
  .brand__name {
    font-family: "Montserrat", sans-serif; font-weight: 800; font-size: 30px;
    color: var(--brand-blue); letter-spacing: .5px; line-height: 1;
  }
  .brand__rule { display: flex; align-items: center; gap: 8px; margin-top: 6px; }
  .brand__rule::before, .brand__rule::after { content: ""; width: 50px; height: 3px; background: var(--brand-blue); }
  .brand__sub {
    font-family: "Montserrat", sans-serif; font-weight: 600; font-size: 12.5px;
    color: var(--brand-gray); letter-spacing: .6px;
  }
  .brand__tagline {
    font-style: italic; font-size: 10px; color: var(--brand-blue);
    margin-top: 4px; margin-left: 60px;
  }

  .property-photo {
    position: absolute; left: 0; top: 160px; width: 572px; height: 300px;
    background: linear-gradient(180deg, var(--photo-sky) 0%, var(--photo-wall) 45%, var(--photo-pool) 78%, var(--photo-lawn) 100%);
  }

  .report-details {
    position: absolute; left: 40px; top: 525px; width: 492px; height: 92px;
    border: 2px solid var(--paper); color: var(--paper); text-align: center;
  }
  .report-details__address {
    position: absolute; left: 50%; top: -15px; transform: translateX(-50%);
    background: var(--brand-blue); padding: 0 10px; white-space: nowrap;
    font-family: "Montserrat", sans-serif; font-weight: 800; font-size: 21px;
  }
  .report-details__list { list-style: none; margin-top: 24px; font-family: "Montserrat", sans-serif; font-weight: 500; font-size: 11px; line-height: 1.6; letter-spacing: .3px; }

  .credentials { position: absolute; left: 42px; top: 640px; display: flex; gap: 14px; }
  .credentials__badge { width: 33px; height: 33px; border-radius: 50%; background: var(--brand-gray); border: 2px solid #d7d9db; }
  .credentials__badge--gold { background: #d8a43a; }
  .credentials__badge--green { background: var(--brand-green); }

  .contact { position: absolute; top: 695px; height: 36px; background: var(--brand-blue); color: var(--paper);
    font-family: "Montserrat", sans-serif; font-weight: 800; display: flex; align-items: center; justify-content: center; white-space: nowrap; }
  .contact--phone { left: 40px; width: 225px; font-size: 23px; }
  .contact--web { left: 278px; width: 254px; font-size: 17px; font-weight: 700; }
</style>
</head>
<body>
  <main class="cover">
    <div class="property-photo" role="img" aria-label="Photograph of the inspected home's exterior"></div>

    <svg class="cover__shapes" viewBox="0 0 572 740" width="572" height="740" aria-hidden="true">
      <polygon points="0,160 382,160 362,198 0,198" fill="var(--brand-blue)"/>
      <polygon points="384,160 428,160 408,198 364,198" fill="var(--brand-green)"/>
      <polygon points="430,160 478,160 454,184" fill="var(--brand-gray)"/>
      <rect x="0" y="462" width="572" height="278" fill="var(--brand-blue)"/>
      <polygon points="318,432 572,432 572,474 296,474" fill="var(--brand-green)"/>
      <polygon points="220,462 282,462 251,492" fill="var(--brand-gray)"/>
      <polygon points="290,438 322,438 286,494 254,494" fill="var(--paper)"/>
      <rect x="0" y="712" width="572" height="28" fill="var(--brand-green)"/>
    </svg>

    <header class="brand">
      <span class="brand__mark"></span>
      <div>
        <div class="brand__name">HARBORVIEW CHECKS</div>
        <div class="brand__rule"><span class="brand__sub">INSPECTION PROFESSIONALS</span></div>
        <div class="brand__tagline">Careful Home Inspections Since 1991</div>
      </div>
    </header>

    <section class="report-details">
      <h1 class="report-details__address">1234 Main Street, Client Town, CT</h1>
      <ul class="report-details__list">
        <li>INSPECTION PREPARED FOR: Dan &amp; Laura Reed</li>
        <li>INSPECTOR: Morgan Hale / License #40918</li>
        <li>DATE OF INSPECTION: 3/7/2020</li>
      </ul>
    </section>

    <div class="credentials" aria-label="Certifications">
      <span class="credentials__badge"></span>
      <span class="credentials__badge credentials__badge--gold"></span>
      <span class="credentials__badge"></span>
      <span class="credentials__badge"></span>
      <span class="credentials__badge credentials__badge--green"></span>
      <span class="credentials__badge credentials__badge--gold"></span>
      <span class="credentials__badge credentials__badge--green"></span>
      <span class="credentials__badge credentials__badge--gold"></span>
      <span class="credentials__badge credentials__badge--green"></span>
      <span class="credentials__badge"></span>
    </div>

    <div class="contact contact--phone">800-555-0147</div>
    <div class="contact contact--web">harborviewchecks.com</div>
  </main>
</body>
</html>
```